Sleek business card design for digital agency.

Brief document attached for detailed description and inspiration. Looking for a minimalist sleek, cool, modern business card design.

Industry/Entity Type

Digital

```html
<!DOCTYPE html>
<html lang="en">
<head>
<meta charset="utf-8">
<title>Flintlock Studio – Business Card</title>
<link href="https://fonts.googleapis.com/css2?family=Mulish:wght@400;600;700&display=swap" rel="stylesheet">
<style>
  :root {
    --backdrop: #3b2419;
    --card: #231f24;
    --card-shadow: rgba(0,0,0,0.45);
    --mark: #121014;
    --text: #f2f2f2;
    --accent: #2a9fd8;
  }
  html, body {
    margin: 0;
    padding: 0;
    width: 1200px;
    height: 1181px;
    overflow: hidden;
    background: var(--backdrop);
    font-family: "Mulish", sans-serif;
  }
  .canvas { position: relative; width: 1200px; height: 1181px; }
  .card {
    position: absolute;
    left: 242px;
    width: 717px;
    height: 412px;
    background: var(--card);
    box-shadow: 0 6px 14px var(--card-shadow);
    overflow: hidden;
  }
  .card--front { top: 148px; }
  .card--back { top: 612px; }

  .brand {
    position: absolute;
    left: 0; right: 0; top: 172px;
    display: flex;
    align-items: center;
    justify-content: center;
    gap: 18px;
    color: var(--mark);
  }
  .brand__dot {
    width: 44px; height: 44px;
    border-radius: 50%;
    background: var(--mark);
  }
  .brand__name {
    font-size: 58px;
    font-weight: 700;
    line-height: 1;
    letter-spacing: 1px;
  }

  .identity {
    position: absolute;
    left: 123px;
    top: 116px;
    color: var(--text);
  }
  .identity__name {
    margin: 0;
    font-size: 25px;
    font-weight: 700;
    letter-spacing: 1.5px;
    line-height: 30px;
  }
  .identity__role {
    margin: 0;
    font-size: 15px;
    font-weight: 600;
    letter-spacing: 2.4px;
    line-height: 19px;
  }
  .identity__note {
    margin: 0;
    font-size: 11.5px;
    font-weight: 600;
    line-height: 15px;
  }
  .divider {
    position: absolute;
    left: 123px;
    top: 188px;
    width: 288px;
    height: 2px;
    background: var(--accent);
  }
  .contacts {
    position: absolute;
    left: 100px;
    top: 201px;
    margin: 0;
    padding: 0;
    list-style: none;
    color: var(--text);
    font-size: 12.5px;
    font-weight: 600;
    letter-spacing: 0.6px;
    line-height: 16.6px;
  }
  .contacts li {
    display: flex;
    align-items: flex-start;
  }
  .contacts__icon {
    flex: none;
    width: 10px; height: 10px;
    margin: 3px 15px 0 0;
    border-radius: 50%;
    background: var(--accent);
  }
</style>
</head>
<body>
<div class="canvas">
  <section class="card card--front" aria-label="Card front">
    <div class="brand">
      <span class="brand__dot"></span>
      <span class="brand__name">Flintlock Studio</span>
    </div>
  </section>

  <section class="card card--back" aria-label="Card back">
    <div class="identity">
      <h1 class="identity__name">Daniel Hartley</h1>
      <p class="identity__role">Marketing Director</p>
      <p class="identity__note">Drink order: G&amp;T with cucumber</p>
    </div>
    <div class="divider"></div>
    <ul class="contacts">
      <li><span class="contacts__icon"></span><span>Level 2, 18 Carrow Lane<br>East Marlow NSW 5100</span></li>
      <li><span class="contacts__icon"></span><span>0400 555 218</span></li>
      <li><span class="contacts__icon"></span><span>03 9555 0142</span></li>
      <li><span class="contacts__icon"></span><span>dhartley@flintlockstudio.com</span></li>
      <li><span class="contacts__icon"></span><span>@dhartley82</span></li>
      <li><span class="contacts__icon"></span><span>social.example/FlintlockStudio</span></li>
    </ul>
  </section>
</div>
</body>
</html>
```